Rack Card for Portuguese Walking Food Tour

I would like a vertical rack card measuring 99x210mm. Here is the information I would like to include. It does not need to be in this format. We are located in Setubal, Portugal.
Please use the attached Teal Heron Logo.
Setúbal: Tradition and Today
Experience the culinary delights of Setúbal, Portugal with a walking food tour around our waterfront village. Discover the Mercado da Gaivota Branca, voted one of the world’s best markets by Metro Ledger, and indulge in local wines and dishes. Prepare for a calm stroll on flat streets. No hills to climb on this tour.
Duration: 4 hours
www.brinebasketwalks.com
+351 265 000 487

```html
<!DOCTYPE html>
<html lang="en">
<head>
<meta charset="utf-8">
<title>Teal Heron Tours – Setúbal Roll-up</title>
<link href="https://fonts.googleapis.com/css2?family=Poppins:wght@500;600&family=Dancing+Script:wght@700&display=swap" rel="stylesheet">
<style>
  :root{
    --orange:#f26522;
    --charcoal:#555556;
    --text-grey:#6a6a6c;
    --white:#ffffff;
    --stage:#e4e4e6;
  }
  html,body{margin:0;padding:0;width:1200px;height:1200px;overflow:hidden;background:var(--stage);}
  .banner{
    position:absolute;left:315px;top:20px;width:780px;height:1590px;
    transform:scale(0.7296);transform-origin:0 0;
    background:var(--white);overflow:hidden;
    font-family:'Poppins',sans-serif;
  }
  .banner-art{position:absolute;left:0;top:0;width:780px;height:1590px;}
  .brand{position:absolute;display:flex;align-items:center;gap:14px;font-weight:600;}
  .brand-dot{border-radius:50%;flex:none;}
  .brand-top{left:412px;top:92px;color:var(--charcoal);font-size:34px;}
  .brand-top .brand-dot{width:56px;height:56px;background:var(--orange);}
  .brand-footer{left:0;right:0;top:1518px;justify-content:center;color:var(--white);font-size:28px;}
  .brand-footer .brand-dot{width:44px;height:44px;background:var(--white);}
  .title-band{
    position:absolute;left:96px;top:218px;width:401px;height:80px;background:var(--orange);
    display:flex;align-items:center;padding-left:22px;box-sizing:border-box;
  }
  .title-band h1{margin:0;font-family:'Dancing Script',cursive;font-weight:700;font-size:34px;color:var(--white);}
  .intro{
    position:absolute;left:163px;top:316px;width:455px;margin:0;
    font-size:21px;line-height:29.8px;font-weight:500;color:var(--text-grey);text-align:justify;
  }
  .facts{
    position:absolute;left:22px;right:22px;top:1452px;display:flex;justify-content:space-between;
    font-size:18.5px;font-weight:600;color:var(--orange);
  }
  .fact{display:flex;align-items:center;gap:8px;}
  .fact svg{width:23px;height:23px;flex:none;}
</style>
</head>
<body>
<div class="banner">
  <svg class="banner-art" viewBox="0 0 780 1590" xmlns="http://www.w3.org/2000/svg">
    <path d="M0 0 H293 C170 90 70 260 70 470 C70 570 90 640 120 690 L0 775 Z" fill="#f26522"/>
    <path d="M0 770 C200 1010 520 1110 780 1050 L780 1095 C540 1200 220 1190 0 1110 Z" fill="#555556"/>
    <path d="M600 1092 C670 1085 730 1070 780 1050 L780 1092 C730 1110 670 1120 610 1125 Z" fill="#f26522"/>
    <circle cx="190" cy="822" r="168" fill="#f26522"/>
    <g role="img" aria-label="Photo of two glasses of rosé wine on a waterfront table">
      <circle cx="190" cy="822" r="150" fill="#b9865d"/>
    </g>
    <circle cx="517" cy="848" r="212" fill="#f26522"/>
    <g role="img" aria-label="Photo of a traditional Portuguese stew with meats, vegetables and cabbage">
      <circle cx="517" cy="848" r="182" fill="#b98a58"/>
    </g>
    <circle cx="392" cy="1112" r="277" fill="#555556"/>
    <g role="img" aria-label="Photo of fresh red mullet fish at the market">
      <circle cx="392" cy="1112" r="258" fill="#d9967f"/>
    </g>
    <rect x="0" y="1495" width="780" height="95" fill="#555556"/>
  </svg>

  <div class="brand brand-top"><span class="brand-dot"></span>Teal Heron Tours</div>

  <div class="title-band"><h1>Setúbal: Tradition and Today</h1></div>

  <p class="intro">Experience the culinary delights of Setúbal, Portugal with a walking food tour around our waterfront village. Discover the Mercado da Gaivota Branca, voted one of the world’s best markets by Metro Ledger, and indulge in local wines and dishes. Prepare for a calm stroll on flat streets. No hills to climb on this tour.</p>

  <div class="facts">
    <span class="fact">
      <svg viewBox="0 0 24 24"><circle cx="12" cy="12" r="12" fill="#555556"/><circle cx="12" cy="12" r="7" fill="none" stroke="#fff" stroke-width="1.6"/><path d="M12 8 V12 L15 14" fill="none" stroke="#fff" stroke-width="1.6"/></svg>
      Duration: 4 hours
    </span>
    <span class="fact">
      <svg viewBox="0 0 24 24"><circle cx="12" cy="12" r="12" fill="#555556"/><circle cx="12" cy="12" r="7" fill="none" stroke="#fff" stroke-width="1.4"/><ellipse cx="12" cy="12" rx="3" ry="7" fill="none" stroke="#fff" stroke-width="1.4"/><path d="M5 12 H19" stroke="#fff" stroke-width="1.4"/></svg>
      www.brinebasketwalks.com
    </span>
    <span class="fact">
      <svg viewBox="0 0 24 24"><circle cx="12" cy="12" r="12" fill="#555556"/><path d="M8 6 L10.5 6 L11.5 9 L10 10.5 C11 12.5 12 13.5 13.5 14 L15 12.5 L18 13.5 L18 16 C14 18 7 11 8 6 Z" fill="#fff"/></svg>
      +351 265 000 487
    </span>
  </div>

  <div class="brand brand-footer"><span class="brand-dot"></span>Teal Heron Tours</div>
</div>
</body>
</html>
```